Basic Company webpage with the elements and colors of our Logo

Basic Home page with a few pages:
- Home,
- About US,
- Contact us
- Services

Target Market(s)

Business Customers (B2B)

Coding

Coded - Design and coding required

Number of Pages Required

5+ page

Requirements
Must have
• Professional, Clean, Simple High Tech, Contact should have a contact us dialog for sending messages to us
Nice to have
• Meet with us links for calendar access though MS Bookings

```html
<!DOCTYPE html>
<html lang="en">
<head>
<meta charset="UTF-8">
<title>Orbitline Service Group</title>
<link href="https://fonts.googleapis.com/css2?family=Poppins:wght@400;500;600;700;800;900&display=swap" rel="stylesheet">
<style>
:root{
  --navy:#064266;
  --navy-deep:#0b4a6b;
  --heading:#0d4466;
  --gold:#f9b03a;
  --gold-line:#d7a140;
  --text:#5b5b5b;
  --field:#eae8e9;
  --white:#ffffff;
}
*{margin:0;padding:0;box-sizing:border-box}
html,body{width:1200px;height:3328px;overflow:hidden;background:var(--white)}
body{font-family:"Poppins",sans-serif;color:var(--text)}
.page{position:relative;width:1200px;height:3328px;overflow:hidden}
.abs{position:absolute}

/* hero */
.hero{position:absolute;left:0;top:0;width:1200px;height:690px;background:var(--navy);overflow:hidden}
.hero-glow{position:absolute;left:-200px;top:300px;width:560px;height:560px;border-radius:50%;
  background:radial-gradient(circle,rgba(214,168,60,.85) 0%,rgba(120,130,70,.45) 40%,rgba(6,66,102,0) 70%)}
.hero-photo{position:absolute;left:300px;top:96px;width:820px;height:594px;
  background:radial-gradient(ellipse at 62% 55%,#9a3fc4 0%,#7a3aa8 30%,rgba(90,50,140,.6) 55%,rgba(6,66,102,0) 75%)}
.hero-lines{position:absolute;left:0;top:0}
.brand{position:absolute;display:flex;align-items:center;gap:10px;color:var(--white);font-weight:700;letter-spacing:1px}
.brand .dot{width:18px;height:18px;border-radius:50%;background:var(--white)}
.brand-top{left:92px;top:30px;font-size:28px}
.nav{position:absolute;top:40px;display:flex;font-size:14px;font-weight:500;color:var(--white)}
.nav a{position:absolute;white-space:nowrap;color:var(--white);text-decoration:none}
.nav-active{position:absolute;left:603px;top:0;width:25px;height:3px;background:var(--gold)}
.cart{position:absolute;left:882px;top:40px;display:flex;align-items:center;gap:12px;color:var(--white);font-size:15px;font-weight:600}
.btn{position:absolute;display:flex;align-items:center;justify-content:center;border-radius:30px;
  font-weight:600;font-size:14px;text-transform:uppercase;color:var(--white);background:var(--gold)}
.btn-outline{background:transparent;border:2px solid var(--white)}
.hero-title{position:absolute;left:88px;top:192px;font-weight:900;font-size:72px;line-height:80px;color:var(--white);letter-spacing:-2px}

/* about / why */
.photo{position:absolute;border-radius:18px}
.label{position:absolute;left:620px;top:810px;display:flex;align-items:center;gap:12px;color:var(--gold);font-weight:600;font-size:15px}
.label span{display:block;width:32px;height:2px;background:var(--gold)}
.h2{position:absolute;font-weight:700;font-size:36px;color:var(--heading)}
.body{position:absolute;font-size:13px;line-height:22px;color:var(--text)}
.bullets{position:absolute;left:150px;top:1336px;list-style:none;font-size:13px;line-height:27px}
.bullets li{position:relative;padding-left:16px}
.bullets li::before{content:"";position:absolute;left:0;top:11px;width:6px;height:6px;border-radius:50%;background:var(--gold)}

/* services */
.services{position:absolute;left:0;top:1642px;width:1200px;height:691px;
  background:linear-gradient(135deg,#f8b43e 0%,#f6ae3c 50%,#e0a445 70%,#f5ad3b 100%)}
.services-title{position:absolute;left:0;width:1200px;top:1684px;text-align:center;font-weight:700;font-size:36px;color:var(--white)}
.card{position:absolute;width:266px;height:234px;background:var(--white);border-radius:14px}
.card .icon{position:absolute;left:30px;top:22px;width:80px;height:80px;border-radius:50%;background:var(--navy-deep);display:flex;align-items:center;justify-content:center}
.card h3{position:absolute;left:29px;top:114px;font-size:17px;font-weight:700;color:var(--heading);text-transform:uppercase}
.card p{position:absolute;left:29px;top:146px;width:224px;font-size:12px;line-height:22px;color:var(--text)}

/* contact */
.field{position:absolute;background:var(--field);border-radius:28px;font-size:13px;color:#6a6a6a;padding-left:26px;display:flex;align-items:center}
.field-area{align-items:flex-start;padding-top:14px;border-radius:22px}

/* footer */
.footer{position:absolute;left:0;top:2976px;width:1200px;height:352px;background:var(--navy-deep);color:var(--white)}
.footer h4{position:absolute;font-size:24px;font-weight:600;line-height:32px;text-transform:uppercase}
.footer .links{position:absolute;left:435px;top:96px;list-style:none;font-size:13px;line-height:26.5px}
.info{position:absolute;left:682px;font-size:13px;line-height:18px}
.info b{font-weight:600;display:block}
.info svg{position:absolute;left:-20px;top:3px}
.social{position:absolute;width:48px;height:48px;border-radius:50%}
.divider{position:absolute;left:90px;top:295px;width:1021px;height:1px;background:rgba(255,255,255,.2)}
.copy{position:absolute;left:0;width:1200px;top:315px;text-align:center;font-size:13px}
</style>
</head>
<body>
<div class="page">

  <!-- HERO -->
  <section class="hero">
    <div class="hero-glow"></div>
    <div class="hero-photo" role="img" aria-label="Photo of a man in a purple hoodie wearing a virtual reality headset, reaching forward"></div>
    <svg class="hero-lines" width="1200" height="690" viewBox="0 0 1200 690" fill="none" stroke="var(--gold-line)" stroke-width="1.5">
      <path d="M562 0 A72 69 0 0 0 562 138 H1200"/>
      <path d="M947 0 V138"/>
      <path d="M1085 0 V138"/>
      <path d="M1085 138 A175 175 0 0 1 1040 390"/>
    </svg>
    <div class="brand brand-top"><span class="dot"></span>ORBITLINE</div>
    <div class="nav-active"></div>
    <nav class="nav">
      <a style="left:575px">HOME</a>
      <a style="left:653px">ABOUT US</a>
      <a style="left:760px">SERVICES</a>
    </nav>
    <div class="cart">
      <svg width="20" height="22" viewBox="0 0 20 22" fill="none" stroke="var(--gold)" stroke-width="1.6"><path d="M2 6h16l-1 15H3z"/><path d="M6 8V5a4 4 0 0 1 8 0v3"/></svg>
      <span>(0)</span>
    </div>
    <a class="btn" style="left:966px;top:26px;width:145px;height:48px">Contact Us</a>
    <h1 class="hero-title">ORBITLINE<br>SERVICE GROUP</h1>
    <a class="btn" style="left:88px;top:364px;width:217px;height:45px">Explore Our Services</a>
    <a class="btn btn-outline" style="left:320px;top:364px;width:144px;height:45px">Contact Us</a>
  </section>

  <!-- ABOUT -->
  <div class="photo" style="left:151px;top:779px;width:424px;height:322px;background:linear-gradient(120deg,#c7b8a8 0%,#8a7560 40%,#3c3a40 70%,#2a5b78 100%)" role="img" aria-label="Photo of a woman working on a laptop with holographic charts"></div>
  <div class="label"><span></span>ABOUT US</div>
  <h2 class="h2" style="left:620px;top:840px">WHO WE ARE</h2>
  <p class="body" style="left:620px;top:902px;width:430px">Orbitline Service Group is a leading provider of high-tech IT services, committed to empowering businesses through innovative and scalable solutions. Our team of experts brings years of experience and a passion for delivering exceptional results.</p>
  <a class="btn" style="left:621px;top:1014px;width:149px;height:45px">Learn More</a>

  <!-- WHY -->
  <h2 class="h2" style="left:150px;top:1280px">WHY CHOOSE US?</h2>
  <ul class="bullets">
    <li>Proven track record in delivering high-tech solutions.</li>
    <li>Focused on reliability, scalability, and efficiency.</li>
    <li>Dedicated customer support tailored to your needs.</li>
  </ul>
  <a class="btn" style="left:150px;top:1433px;width:148px;height:45px">Learn More</a>
  <div class="photo" style="left:620px;top:1209px;width:424px;height:323px;background:linear-gradient(135deg,#4a2a24 0%,#3a3a48 45%,#2a3550 75%,#5a4a50 100%)" role="img" aria-label="Photo of a man in a VR headset touching a holographic interface"></div>

  <!-- SERVICES -->
  <section class="services"></section>
  <h2 class="services-title">OUR SERVICES</h2>

  <div class="card" style="left:178px;top:1764px">
    <div class="icon"><svg width="42" height="42" viewBox="0 0 42 42" fill="none" stroke="#fff" stroke-width="2"><circle cx="15" cy="14" r="6"/><path d="M4 36c0-7 5-11 11-11s11 4 11 11"/><circle cx="32" cy="30" r="5"/><path d="M26 6h12v8h-8l-3 3v-3"/></svg></div>
    <h3>IT Consulting</h3>
    <p>Providing expert advice to optimize your technology strategies and achieve business goals</p>
  </div>
  <div class="card" style="left:466px;top:1764px">
    <div class="icon"><svg width="42" height="42" viewBox="0 0 42 42" fill="none" stroke="#fff" stroke-width="2"><circle cx="18" cy="13" r="6"/><path d="M18 4v3M18 19v3M9 13h3M24 13h3"/><path d="M4 30h8l8 4 16-8v4l-16 8-8-3H4z"/></svg></div>
    <h3>IT Services</h3>
    <p>Comprehensive IT support and maintenance to ensure your systems run smoothly 24/7.</p>
  </div>
  <div class="card" style="left:756px;top:1764px">
    <div class="icon"><svg width="44" height="42" viewBox="0 0 44 42" fill="none" stroke="#fff" stroke-width="2"><path d="M12 24a7 7 0 0 1 1-14 9 9 0 0 1 17 2 6 6 0 0 1 2 12z"/><path d="M14 24v8M22 24v10M30 24v8"/><circle cx="14" cy="34" r="2"/><circle cx="22" cy="36" r="2"/><circle cx="30" cy="34" r="2"/></svg></div>
    <h3>Cloud Solutions</h3>
    <p>Seamless migration and management of your business operations on the cloud.</p>
  </div>
  <div class="card" style="left:178px;top:2020px">
    <div class="icon"><svg width="42" height="42" viewBox="0 0 42 42" fill="none" stroke="#fff" stroke-width="2"><path d="M21 4l13 5v10c0 9-6 15-13 18C14 34 8 28 8 19V9z"/><rect x="15" y="18" width="12" height="9" rx="1"/><path d="M17 18v-3a4 4 0 0 1 8 0v3"/></svg></div>
    <h3>Cybersecurity</h3>
    <p>Advanced solutions to protect your business from cyber threats and vulnerabilities.</p>
  </div>
  <div class="card" style="left:466px;top:2020px">
    <div class="icon"><svg width="42" height="42" viewBox="0 0 42 42" fill="none" stroke="#fff" stroke-width="2"><path d="M34 21a13 13 0 0 1-22 9M8 21a13 13 0 0 1 22-9"/><path d="M30 6v6h-6M12 36v-6h6"/><circle cx="21" cy="21" r="5"/></svg></div>
    <h3>Development</h3>
    <p>Custom software tailored to meet your unique business requirements.</p>
  </div>
  <div class="card" style="left:756px;top:2020px">
    <div class="icon"><svg width="42" height="42" viewBox="0 0 42 42" fill="none" stroke="#fff" stroke-width="2"><rect x="5" y="7" width="30" height="21" rx="1"/><path d="M14 36h12M20 28v8"/><path d="M11 23v-5M16 23v-9M21 23v-7M26 23v-11"/><circle cx="32" cy="26" r="4"/><path d="M35 29l4 4"/></svg></div>
    <h3>Data Analytics</h3>
    <p>Transforming data into actionable insights to drive smarter decisions.</p>
  </div>

  <!-- CONTACT -->
  <h2 class="h2" style="left:0;width:1200px;text-align:center;top:2420px">GET IN TOUCH WITH US</h2>
  <p class="body" style="left:270px;width:660px;top:2476px;text-align:center;line-height:20px">Have questions about our services or need a quote for your flooring maintenance needs? Our team is ready to assist you. Simply fill out the form below, and we'll get back to you as soon as possible.</p>
  <div class="field" style="left:223px;top:2547px;width:369px;height:57px">First Name</div>
  <div class="field" style="left:607px;top:2547px;width:369px;height:57px">Last Name</div>
  <div class="field" style="left:223px;top:2621px;width:369px;height:57px">E mail</div>
  <div class="field" style="left:607px;top:2621px;width:369px;height:57px">Phone</div>
  <div class="field field-area" style="left:223px;top:2693px;width:753px;height:123px">How Can We Help You ?</div>
  <a class="btn" style="left:532px;top:2837px;width:138px;height:41px;font-size:15px">Submit</a>

  <!-- FOOTER -->
  <footer class="footer">
    <div class="brand" style="left:92px;top:126px;font-size:34px"><span class="dot" style="width:22px;height:22px"></span>ORBITLINE</div>
    <h4 style="left:435px;top:52px">Quick Link</h4>
    <ul class="links">
      <li>Home</li><li>About Us</li><li>Services</li><li>Contact Us</li>
    </ul>
    <h4 style="left:661px;top:54px">Contact Us</h4>
    <div class="info" style="top:98px">
      <svg width="12" height="12" viewBox="0 0 12 12" fill="var(--gold)"><path d="M2 0l3 3-1.5 1.5a7 7 0 0 0 4 4L9 7l3 3-2 2C5 12 0 7 0 2z"/></svg>
      <b>Phone</b>(123) 456-7890
    </div>
    <div class="info" style="top:144px">
      <svg width="12" height="10" viewBox="0 0 12 10" fill="var(--gold)"><path d="M0 0h12v10H0z"/><path d="M0 0l6 5 6-5" stroke="#0b4a6b" fill="none"/></svg>
      <b>Email</b>info@example.com
    </div>
    <div class="info" style="top:190px">
      <svg width="12" height="16" viewBox="0 0 12 16" fill="var(--gold)"><path d="M6 0a6 6 0 0 1 6 6c0 4-6 10-6 10S0 10 0 6a6 6 0 0 1 6-6z"/><circle cx="6" cy="6" r="2" fill="#0b4a6b"/></svg>
      <b>Address</b>9123 Tech Park, Business City
    </div>
    <h4 style="left:953px;top:54px">Follow Us</h4>
    <div class="social" style="left:955px;top:100px;background:var(--gold)" aria-label="Social profile"></div>
    <div class="social" style="left:1009px;top:100px;background:#1d5a7d" aria-label="Social profile"></div>
    <div class="social" style="left:1062px;top:100px;background:#1d5a7d" aria-label="Social profile"></div>
    <div class="divider"></div>
    <p class="copy">© Copyrights 2024, Orbitline Service Group, All Rights Reserved</p>
    <svg class="abs" style="left:1126px;top:270px" width="50" height="44" viewBox="0 0 50 44">
      <path d="M8 4h26a6 6 0 0 1 6 6v14a6 6 0 0 1-6 6H18l-10 8v-8a6 6 0 0 1-6-6V10a6 6 0 0 1 6-6z" fill="var(--gold)"/>
      <circle cx="14" cy="17" r="2.5" fill="#fff"/><circle cx="21" cy="17" r="2.5" fill="#fff"/><circle cx="28" cy="17" r="2.5" fill="#fff"/>
    </svg>
  </footer>
</div>
</body>
</html>
```